car wrap design 2019 Vantrel 170WB high roof white color

Im looking for a catchy but simple car wrap design for a van 2019Mercedes Vantrel Van 170 WB . Its a Heating and Cooling company specializing in the residential market. Installation, service and maintenance of all heating and Cooling equipment . Van is white and im looking for a partial wrap with 3 other colours red ,blue and grey. Something simple my name "The Frostline Heating and Cooling " website "thefrostline.ca phone nr "555-314-2087 and logo and description of what im doing . .

Industry/Entity Type

Hvac

Colors

Designer to choose colors to be used in the design.

Requirements
Must have
• big logo see file attached phone nr 555-314-2087 web. thefrostline.ca
Nice to have
• stand out logo visible ,phone nr
Should not have
• too many colours max 4 colours white red blue and maybe gray. no curvy lines

```html
<!DOCTYPE html>
<html lang="en">
<head>
<meta charset="utf-8">
<title>The Frostline Heating and Cooling — Van Wrap</title>
<link rel="stylesheet" href="https://fonts.googleapis.com/css2?family=Passion+One:wght@700&family=Nunito:wght@800&display=swap">
<style>
  :root {
    --canvas: #eeeeee;
    --van-white: #ffffff;
    --panel-line: #c9ccd0;
    --trim: #2b2b2d;
    --glass: #3a3f44;
    --tyre: #1e1e1f;
    --rim: #9a9ea3;
    --wrap-blue: #1e9fd6;
    --wrap-red: #e1322b;
    --brand-red: #e43a26;
    --web-blue: #1e8fb8;
    --phone-red: #e4472a;
  }
  html, body {
    margin: 0;
    width: 1200px;
    height: 1200px;
    overflow: hidden;
    background: var(--canvas);
  }
  .wrap-sheet { display: block; width: 1200px; height: 1200px; }
  .van-body { fill: var(--van-white); stroke: var(--panel-line); stroke-width: 1.5; }
  .panel-seam { stroke: var(--panel-line); stroke-width: 1.5; fill: none; }
  .rub-strip { fill: var(--trim); }
  .bumper { fill: var(--trim); }
  .cab-window { fill: var(--glass); }
  .door-handle { fill: var(--trim); }
  .tyre { fill: var(--tyre); }
  .rim { fill: var(--rim); stroke: #6d7175; stroke-width: 2; }
  .rear-lamp { fill: var(--wrap-red); }
  .wrap-blue { fill: var(--wrap-blue); }
  .wrap-red { fill: var(--wrap-red); }
  .hero-art { fill: url(#heroTone); }
  .brand-name {
    font-family: "Passion One", "Arial Black", sans-serif;
    font-weight: 700;
    fill: var(--brand-red);
  }
  .brand-tag {
    font-family: "Passion One", "Arial Black", sans-serif;
    font-weight: 700;
    fill: var(--brand-red);
  }
  .web-address {
    font-family: "Nunito", Arial, sans-serif;
    font-weight: 800;
    fill: var(--web-blue);
  }
  .phone-number {
    font-family: "Nunito", Arial, sans-serif;
    font-weight: 800;
    fill: var(--phone-red);
    letter-spacing: 1px;
  }
  .icon-disc-web { fill: var(--brand-red); }
  .icon-disc-phone { fill: var(--web-blue); }
  .icon-glyph { fill: none; stroke: #fff; stroke-width: 1.6; }
  .icon-glyph-fill { fill: #fff; }
</style>
</head>
<body>
<svg class="wrap-sheet" viewBox="0 0 1000 1000" xmlns="http://www.w3.org/2000/svg">
  <defs>
    <linearGradient id="fadeToWhite" x1="0" x2="1" y1="0" y2="0">
      <stop offset="0" stop-color="#f2cfae"/>
      <stop offset="0.7" stop-color="#f7e2cd"/>
      <stop offset="1" stop-color="#ffffff" stop-opacity="0"/>
    </linearGradient>
    <linearGradient id="heroTone" x1="0" x2="1" y1="0" y2="1">
      <stop offset="0" stop-color="#f4d2b2"/>
      <stop offset="0.5" stop-color="#eebd92"/>
      <stop offset="1" stop-color="#6f9bcb"/>
    </linearGradient>
    <clipPath id="bodyClip">
      <path d="M40 100 Q42 88 58 86 L790 84 Q812 84 822 100 L905 230 Q960 250 982 292 L986 392 L36 392 Z"/>
    </clipPath>

    <g id="van-side">
      <path class="van-body" d="M40 100 Q42 88 58 86 L790 84 Q812 84 822 100 L905 230 Q960 250 982 292 L986 392 L36 392 Z"/>
      <g clip-path="url(#bodyClip)">
        <rect x="36" y="84" width="420" height="320" fill="url(#fadeToWhite)"/>
        <polygon class="wrap-blue" points="36,84 190,84 150,260 36,300"/>
        <polygon class="wrap-red" points="36,300 150,260 210,400 36,400"/>
        <rect class="hero-art" x="120" y="88" width="220" height="304" rx="12"
              role="img" aria-label="Cartoon superhero mascot in costume running forward"/>
      </g>
      <rect class="rear-lamp" x="34" y="258" width="10" height="76"/>
      <line class="panel-seam" x1="438" y1="86" x2="438" y2="392"/>
      <line class="panel-seam" x1="662" y1="86" x2="662" y2="392"/>
      <path class="panel-seam" d="M812 100 L812 392"/>
      <path class="cab-window" d="M682 142 L790 142 Q806 144 816 160 L840 250 L682 258 Z"/>
      <rect class="door-handle" x="680" y="272" width="40" height="7" rx="3"/>
      <rect class="door-handle" x="825" y="272" width="28" height="7" rx="3"/>
      <rect class="rub-strip" x="36" y="338" width="950" height="30"/>
      <rect class="bumper" x="930" y="348" width="58" height="56" rx="8"/>
      <rect class="bumper" x="32" y="340" width="24" height="56" rx="4"/>
      <circle class="tyre" cx="245" cy="410" r="52"/>
      <circle class="rim" cx="245" cy="410" r="28"/>
      <circle class="tyre" cx="865" cy="410" r="52"/>
      <circle class="rim" cx="865" cy="410" r="28"/>
    </g>
  </defs>

  <g class="van-view van-view--passenger">
    <use href="#van-side"/>
    <text class="brand-name" x="345" y="184" font-size="44" textLength="295" lengthAdjust="spacingAndGlyphs">THE FROSTLINE</text>
    <text class="brand-tag" x="345" y="202" font-size="19" textLength="295" lengthAdjust="spacing">HEATING AND COOLING</text>
    <g class="contact-web">
      <circle class="icon-disc-web" cx="421" cy="222" r="10"/>
      <circle class="icon-glyph" cx="421" cy="222" r="5.5"/>
      <line class="icon-glyph" x1="415.5" y1="222" x2="426.5" y2="222"/>
      <text class="web-address" x="443" y="231" font-size="24">thefrostline.ca</text>
    </g>
    <g class="contact-phone">
      <circle class="icon-disc-phone" cx="421" cy="270" r="10"/>
      <path class="icon-glyph-fill" d="M416 264 q2 -2 4 0 l1 3 q0 2 -2 2 q1 3 4 4 q0 -2 2 -2 l3 1 q2 2 0 4 q-2 2 -5 1 q-6 -3 -8 -9 q-1 -3 1 -4z"/>
      <text class="phone-number" x="438" y="280" font-size="26">555-314-2087</text>
    </g>
  </g>

  <g class="van-view van-view--driver">
    <use href="#van-side" transform="translate(1000 500) scale(-1 1)"/>
    <text class="brand-name" x="360" y="684" font-size="44" textLength="295" lengthAdjust="spacingAndGlyphs">THE FROSTLINE</text>
    <text class="brand-tag" x="360" y="702" font-size="19" textLength="295" lengthAdjust="spacing">HEATING AND COOLING</text>
    <g class="contact-web">
      <text class="web-address" x="370" y="730" font-size="24">thefrostline.ca</text>
      <circle class="icon-disc-web" cx="577" cy="721" r="10"/>
      <circle class="icon-glyph" cx="577" cy="721" r="5.5"/>
      <line class="icon-glyph" x1="571.5" y1="721" x2="582.5" y2="721"/>
    </g>
    <g class="contact-phone">
      <text class="phone-number" x="365" y="780" font-size="26">555-314-2087</text>
      <circle class="icon-disc-phone" cx="578" cy="770" r="10"/>
      <path class="icon-glyph-fill" d="M573 764 q2 -2 4 0 l1 3 q0 2 -2 2 q1 3 4 4 q0 -2 2 -2 l3 1 q2 2 0 4 q-2 2 -5 1 q-6 -3 -8 -9 q-1 -3 1 -4z"/>
    </g>
  </g>
</svg>
</body>
</html>
```